Zielgruppe
Köderhaus Brenkmann in Hamburg ist ein Fachgeschäft mit 450m² Verkaufsfläche für Profi- und Hoppyangler, auch Neueinsteiger werden hier kompetent und bestens beraten. Das Fachgeschäft setzt seinen Schwerpunkt auf ein umfangreiches Sortiment mit den Markenprodukten namenhafter Hersteller und eine kompetente und faire Beratung durch geschultes Fachpersonal.
Das Köderhaus Brenkmann bietet seinen Kunden auf 450m² ein riesiges Sortiment an. Hier finden die Kunden alles was ein Anglerherz höher schlagen lässt. Vom Raubfischangeln mit exklusiven Ködern aus den USA und Japan, sowie Forellen-, Friedfisch-, Meerforellen-, Karpfenangeln und selbstverständlich das Meeresangeln gehören zu dem Hauptsortiment.
Des Weiteren können unsere Kunden ein Teil unseres Sortiments auch bequem über unseren Online-Shop auf www.koederhaus-brenkmann.de bestellen.
Mit dem Elbwelle Brasse (www.elbwelle-brasse.de), unserer Eigenentwicklung eines Gummifisches, möchten wir unser neues Produkt in den Markt einführen.
Designer aus Hamburg?", kommen Sie gerne vorbei, besuchen Sie uns und lassen Sie sich von unserem Köderhaus Brenkmann begeistern.
Wir freuen uns auf Sie,
Markus & Roswitha & das ganze Team
Aufgabenstellung
Bitte unbedingt die Dateien "materialsammlung.zip" und "bitte_diese_design_anleitung_beachten.txt" herunterladen und beachten!
In jedem Fall bei der Designentwicklung folgende Vorgaben beachten und verwenden:
• Tanzende Figuren (Maennchen.psd)
• Skyline von Hamburg (Skyline.psd)
• den „Hintergrundschein“ der durch das Bild geht
• Hintergrundfarbe bitte gemischt aus den Layouts der Flyer aus den vergangenen Aktionen, PINK, NEONGRÜN, etc.
Es müssen insgesamt 3 Seiten entworfen werden:
Die Shop-Startseite, Produktdetailseite und eine Landingpage (jeweils nur das Design der Website als Photoshop-Dokumente).
Die Breite der Website soll später 1000 Pixel betragen. Bitte die Photoshop-Dateien so erstellen, dass diese 1:1 verwendet werden können.
Die Shop-Startseite unter http://www.koederhaus-brenkmann.de/index.php sollte unsere aktuellen Ladenbilder (ggf. in Form eines sliders) beinhalten.
Die Produktdetailseite unter http://www.koederhaus-brenkmann.de/product_info.php?info=p783_Tarolin-KR-8821-Wirbel.html zum Einkauf einladen.
Von www.elbwelle-brasse.de soll auf eine Landingpage im Shop umgeleitet werden, die die Vorteile unserer Neuentwicklung ins rechte Licht rücken soll (siehe Flyer elbwelle-brasse).

```html
<!DOCTYPE html>
<html lang="de">
<head>
<meta charset="utf-8">
<title>Köderhaus Brenkmann – Online-Shop</title>
<link href="https://fonts.googleapis.com/css2?family=PT+Sans:wght@400;700&family=Open+Sans:wght@400;600;700&family=Lora:ital@0;1&display=swap" rel="stylesheet">
<style>
  :root {
    --green: #5aa61e;
    --text: #444;
    --heading: #555;
    --link: #2a9fd6;
    --section-light: #f6f6f6;
    --section-mid: #efefef;
  }
  * { margin: 0; padding: 0; box-sizing: border-box; }
  html, body { width: 910px; height: 1200px; overflow: hidden; background: #fff; }
  body { position: relative; font-family: Arial, Helvetica, sans-serif; color: var(--text); }
  .abs { position: absolute; }

  /* Header */
  .brand { left: 86px; top: 76px; font-family: "PT Sans", sans-serif; font-weight: 700; font-size: 27px; line-height: 1; color: var(--green); white-space: nowrap; }
  .nav { left: 369px; top: 67px; width: 458px; height: 46px; border-top: 1px dotted #555; border-bottom: 1px dotted #555; }
  .nav ul { list-style: none; display: flex; align-items: center; height: 100%; font-family: "PT Sans", sans-serif; font-weight: 700; font-size: 13.5px; color: #444; }
  .nav .active { background: var(--green); color: #fff; width: 84px; height: 37px; display: flex; align-items: center; justify-content: center; margin-left: 3px; }
  .nav .sep { margin-left: 28px; }
  .nav .item { margin-left: 24px; }
  .nav .item.wk { margin-left: 32px; }

  /* Hero */
  .hero { left: 0; top: 173px; width: 910px; height: 280px; background: linear-gradient(180deg, #3e6e2e 0%, #4f7f3a 20%, #3a98bd 32%, #46a9cc 70%, #3d9fc2 100%); }
  .hero-band { left: 0; top: 453px; width: 910px; height: 11px; background: var(--green); }
  .hero-box { left: 86px; top: 226px; width: 398px; height: 162px; background: rgba(90,166,30,0.93); color: #fff; font-family: "Open Sans", sans-serif; }
  .hero-box h1 { position: absolute; left: 16px; top: 30px; font-size: 23px; font-weight: 700; }
  .hero-box h2 { position: absolute; left: 18px; top: 62px; font-size: 14px; font-weight: 700; letter-spacing: 0.3px; }
  .hero-box p { position: absolute; left: 18px; top: 81px; font-size: 14px; letter-spacing: 1.6px; }
  .read-more { left: 369px; top: 343px; }
  .slide-tab { top: 432px; width: 27px; height: 38px; }

  /* Products */
  .products { left: 0; top: 464px; width: 910px; height: 486px; background: var(--section-light); }
  .card { top: 505px; width: 222px; height: 138px; background: #fff; border: 1px solid #ddd; box-shadow: 0 3px 3px rgba(0,0,0,0.12); }
  .card .photo { position: absolute; left: 6px; top: 6px; width: 208px; height: 125px; }
  .card .tag { position: absolute; left: 6px; top: 59px; width: 83px; height: 20px; background: var(--green); color: #fff; font-family: "Open Sans", sans-serif; font-weight: 700; font-size: 8.5px; padding: 5px 0 0 7px; }
  .learn-more { top: 665px; width: 133px; height: 33px; background: var(--green); color: #fff; font-size: 18px; display: flex; align-items: center; justify-content: center; }

  .intro-title { left: 84px; top: 762px; font-family: "Open Sans", sans-serif; font-weight: 600; font-size: 15px; color: var(--heading); }
  .intro-text { left: 86px; top: 793px; width: 432px; font-size: 11.3px; line-height: 13.7px; color: #444; }
  .intro-text a { color: var(--link); text-decoration: none; }
  .intro-text .gap { margin-top: 14px; }

  .events { left: 644px; top: 745px; width: 180px; height: 182px; background: #fff; box-shadow: 0 0 4px rgba(0,0,0,0.15); }
  .events h3 { position: absolute; left: 10px; top: 9px; width: 163px; height: 40px; background: var(--green); color: #fff; font-family: "Open Sans", sans-serif; font-weight: 700; font-size: 12.5px; padding: 12px 0 0 11px; }
  .events ul { list-style: none; position: absolute; left: 11px; top: 60px; width: 160px; }
  .events li { color: var(--link); font-size: 10.8px; line-height: 13px; padding-bottom: 6px; margin-bottom: 7px; border-bottom: 1px solid #4aa8d8; }
  .events li:last-child { border-bottom: none; }

  /* Lower */
  .lower { left: 0; top: 950px; width: 910px; height: 184px; background: var(--section-mid); }
  .t-rule { top: 990px; height: 1px; background: linear-gradient(90deg, rgba(0,0,0,0), #bbb); }
  .t-label { left: 227px; top: 984px; font-family: "Lora", serif; font-size: 10px; color: #d9542b; }
  .avatar { left: 94px; top: 1008px; width: 86px; height: 86px; border-radius: 50%; border: 1px dashed #bbb; padding: 4px; }
  .avatar .photo { width: 100%; height: 100%; border-radius: 50%; background: radial-gradient(circle at 50% 40%, #7a8794, #3d4650); }
  .quote { left: 184px; top: 1011px; font-family: "Lora", serif; font-style: italic; font-size: 12px; line-height: 18.2px; color: #444; }
  .quote .mark { color: #bbb; font-size: 14px; }
  .quote-author { left: 230px; top: 1073px; width: 124px; text-align: center; font-family: "Lora", serif; font-size: 9.5px; color: #555; line-height: 15px; }
  .quote-author .company { font-family: Arial, sans-serif; color: #1d4f8a; font-size: 10px; }

  .sub-title { left: 579px; top: 980px; font-family: "Open Sans", sans-serif; font-weight: 700; font-size: 16.5px; color: var(--green); }
  .sub-text { left: 589px; top: 1003px; width: 240px; font-size: 6.8px; line-height: 10px; color: #888; }
  .field { top: 1045px; width: 113px; height: 19px; background: #fff; border: 1px solid #ddd; font-size: 8.5px; color: #999; padding: 4px 7px; }
  .check { left: 592px; top: 1087px; font-size: 7.5px; color: #777; display: flex; align-items: center; gap: 5px; }
  .check .box { width: 10px; height: 10px; border: 1px solid #bbb; background: #fff; }
  .subscribe { left: 733px; top: 1080px; width: 89px; height: 21px; background: var(--green); color: #fff; font-size: 12px; display: flex; align-items: center; justify-content: center; gap: 6px; }

  .footer { left: 0; top: 1134px; width: 910px; height: 66px; background: var(--green); }
  .copyright { left: 87px; top: 1164px; font-family: "Open Sans", sans-serif; font-size: 9.5px; color: #fff; }
  .social { left: 724px; top: 1163px; display: flex; gap: 4px; }
  .social span { width: 13px; height: 13px; background: #e9f2f8; border: 1px solid #9fb7cc; display: block; }
</style>
</head>
<body>

<header>
  <div class="abs brand">Köderhaus Brenkmann</div>
  <nav class="abs nav">
    <ul>
      <li class="active">ANMELDEN</li>
      <li class="sep">|</li>
      <li class="item">IHR KONTO</li>
      <li class="item">|</li>
      <li class="item wk">WARENKORB</li>
      <li class="item">|</li>
      <li class="item">KASSE</li>
    </ul>
  </nav>
</header>

<section>
  <div class="abs hero" role="img" aria-label="Seeadler greift über blauem See mit bewaldetem Ufer nach einem Fisch"></div>
  <div class="abs hero-band"></div>
  <div class="abs hero-box">
    <h1>BRENKMANN’S</h1>
    <h2>ELBWELLE BRASSE</h2>
    <p>DER ULTIMATIVE GUMMIFISCH</p>
  </div>
  <svg class="abs read-more" width="88" height="28" viewBox="0 0 88 28">
    <path d="M0 2 Q0 0 2 0 H80 L88 14 L80 28 H2 Q0 28 0 26 Z" fill="#ececec"/>
    <text x="9" y="18.5" font-family="Open Sans, sans-serif" font-weight="700" font-size="11" fill="#333">READ MORE</text>
  </svg>
  <svg class="abs slide-tab" style="left:679px" viewBox="0 0 27 38"><path d="M0 8 L13.5 0 L27 8 V38 H0 Z" fill="#e6e6e6"/><text x="13.5" y="27" text-anchor="middle" font-family="Open Sans, sans-serif" font-weight="700" font-size="14" fill="#666">1</text></svg>
  <svg class="abs slide-tab" style="left:726px" viewBox="0 0 27 38"><path d="M0 8 L13.5 0 L27 8 V38 H0 Z" fill="#e6e6e6"/><text x="13.5" y="27" text-anchor="middle" font-family="Open Sans, sans-serif" font-weight="700" font-size="14" fill="#666">2</text></svg>
  <svg class="abs slide-tab" style="left:771px" viewBox="0 0 27 38"><path d="M0 8 L13.5 0 L27 8 V38 H0 Z" fill="#e6e6e6"/><text x="13.5" y="27" text-anchor="middle" font-family="Open Sans, sans-serif" font-weight="700" font-size="14" fill="#666">3</text></svg>
</section>

<main>
  <div class="abs products"></div>

  <div class="abs card" style="left:85px">
    <div class="photo" role="img" aria-label="Verpackung des Gummifisch-Köders in Rot und Gelbgrün" style="background:linear-gradient(180deg,#c8202a 0%,#b9b72a 45%,#8ea020 100%)"></div>
    <div class="tag">PRODUCT</div>
  </div>
  <div class="abs card" style="left:342px">
    <div class="photo" role="img" aria-label="Angler auf einem Boot hält einen großen Hecht" style="background:linear-gradient(180deg,#5d8fc4 0%,#3f6b9c 50%,#2f4f78 100%)"></div>
    <div class="tag">PRODUCT</div>
  </div>
  <div class="abs card" style="left:603px">
    <div class="photo" role="img" aria-label="Grüne Fliege mit Haken auf einem Stein" style="background:linear-gradient(180deg,#c9c6bf 0%,#b7ad94 60%,#8f7d5e 100%)"></div>
    <div class="tag">PRODUCT</div>
  </div>

  <div class="abs learn-more" style="left:133px">Learn More</div>
  <div class="abs learn-more" style="left:381px">Learn More</div>
  <div class="abs learn-more" style="left:650px">Learn More</div>

  <h2 class="abs intro-title">LOREM IPSUM DOLOR SIT AMET</h2>
  <div class="abs intro-text">
    <p>Lorem ipsum dolor sit amet, consectetur adipiscing elit. Etiam tristique tristique lacus in varius. Donec nec vestibulum ligula. Aenean turpis diam, feugiat a luctus in, rhoncus eget risus.<br>
    Lorem ipsum dolor sit amet, <a href="#">consectetur adipiscing</a> elit. Etiam tristique tristique lacus in varius. Donec nec vestibulum ligula. Aenean turpis diam, feugiat a luctus in, rhoncus eget risus.</p>
    <p class="gap">Auf Langstreckenflügen waren Brille und Kontaktlinsen einfach mühsam. Und in den Badeferien haben sich Strand und Kontaktlinsen auch nicht gut vertragen. Als mir Dr.</p>
  </div>

  <aside class="abs events">
    <h3>INFORMATION EVENT</h3>
    <ul>
      <li>Mo, 27. Januar 2014, 17.30 Uhr<br>Sehzentrum Bergtal</li>
      <li>Do, 13. Februar 2014, 17.30 Uhr<br>Sehzentrum Bergtal</li>
      <li>Do, 6. März 2014, 19.30 Uhr<br>Stadtsaal Haldenau, Marktplatz</li>
    </ul>
  </aside>
</main>

<section>
  <div class="abs lower"></div>

  <div class="abs t-rule" style="left:96px;width:128px"></div>
  <div class="abs t-rule" style="left:353px;width:126px;background:linear-gradient(90deg,#bbb,rgba(0,0,0,0))"></div>
  <div class="abs t-label">FEATURED TESTIMONIAL</div>
  <div class="abs avatar"><div class="photo" role="img" aria-label="Angler mit gefangener Forelle"></div></div>
  <blockquote class="abs quote">
    <span class="mark">“</span> Lorem ipsum dolor sit amet, sanctus<br>
    &nbsp;&nbsp;&nbsp;&nbsp;corrumpit ei quo, eu quo meis brute,<br>
    &nbsp;&nbsp;&nbsp;&nbsp;sed ut possit vocibus graeci manda- <span class="mark">”</span>
  </blockquote>
  <div class="abs quote-author"><span class="company">Nordlicht Medien</span><br>Network Solutions</div>

  <svg class="abs" style="left:516px;top:980px" width="61" height="61" viewBox="0 0 61 61">
    <circle cx="30.5" cy="30.5" r="30" fill="#d8d8d8"/>
    <circle cx="30.5" cy="30.5" r="25" fill="#5aa61e"/>
    <rect x="17" y="21" width="27" height="19" fill="none" stroke="#fff" stroke-width="2.2"/>
    <path d="M17 21 L30.5 32 L44 21 M17 40 L26 30 M44 40 L35 30" fill="none" stroke="#fff" stroke-width="2.2"/>
  </svg>
  <h3 class="abs sub-title">Subscribe to our lates products</h3>
  <p class="abs sub-text">Lorem Ipsum is simply dummy text of the printing and typesetting industry. Lorem Ipsum has been the industry's standard dummy text ever since the 1500s, when an unknown printer took</p>
  <div class="abs field" style="left:589px">Name</div>
  <div class="abs field" style="left:711px">email address</div>
  <div class="abs check"><span class="box"></span>Daily Newsletter</div>
  <div class="abs subscribe">
    <svg width="11" height="11" viewBox="0 0 11 11"><circle cx="5.5" cy="5.5" r="5.5" fill="#fff"/><path d="M3 5.6 L4.9 7.4 L8.2 3.8" fill="none" stroke="#5aa61e" stroke-width="1.6"/></svg>
    Subscribe
  </div>
</section>

<footer>
  <div class="abs footer"></div>
  <p class="abs copyright">© Copyright 2013 koederhaus-brenkmann.de. All Right Reserved</p>
  <div class="abs social"><span></span><span></span><span></span><span></span><span></span><span></span></div>
</footer>

</body>
</html>
```